Grafic Ad for a Printmagazine about Tractor Vehicles

We need for a Geman Printmagazine about Tractors a Grafic Design in different sizes. Our Website and corporate Design: https://www.kalvoro.de You can work with the uploaded files . The round Logo with shaking hands should be included in your Designs somehow. Perhaps as a transparent in the background or placed in a corner. The Font used for the URL is Days (typlume.com/days.font) Please use this Font or a other similar for the URL "kalvoro.de" and expand it to "www.kalvoro.de/traktorwert" For the other Text parts (first line) and (second line) you can use a other font which you prefer. We need the grafics as .jpg in the pixel sizes: 472x496, 437x614, 307x437 (Print would be DPI 300). Goal is a eye-catching design for the later print ad. Have fun and be creative ;)

Logo Text

"Traktor Bewertung" (first line), " Kurzgutachen für Verkauf, Kauf oder Versicherung" (second line), "www.kalvoro.de/traktorwert" (third line)

Logo styles of interest
Pictorial/Combination Logo
Other font styles liked:
• Days.tff for the URL

Colors
0054AA
0677BA
7BADD7
CADEEF
E8F1F8
0094D4
00A9DD
6FCCEA
C7EBF8
E9F6FB

```html
<!DOCTYPE html>
<html lang="de">
<head>
<meta charset="utf-8">
<title>Traktor Bewertung – Anzeigen</title>
<link href="https://fonts.googleapis.com/css2?family=Days+One&display=swap" rel="stylesheet">
<style>
  :root {
    --page: #e7e7e7;
    --white: #ffffff;
    --ink: #4a4a4a;
    --brand-blue: #0677ba;
    --blue-deep: #1a84c6;
    --photo-a: #2f5fa8;
    --photo-b: #8fc3e8;
  }
  * { box-sizing: border-box; margin: 0; padding: 0; }
  html, body { width: 1200px; height: 2371px; overflow: hidden; }
  body {
    background: var(--page);
    position: relative;
    font-family: "Days One", sans-serif;
  }

  .ad { position: absolute; overflow: hidden; background: var(--white); }
  .ad--wide  { left: 97px;  top: 94px;   width: 989px; height: 704px; }
  .ad--tall  { left: 191px; top: 882px;  width: 800px; height: 759px; }
  .ad--small { left: 239px; top: 1735px; width: 705px; height: 494px; }

  .ad__bg { position: absolute; inset: 0; width: 100%; height: 100%; }
  .ad > *:not(.ad__bg) { position: absolute; }

  .brand { display: flex; flex-direction: column; align-items: center; }
  .brand__dot { border-radius: 50%; background: var(--brand-blue); }
  .brand__name { color: var(--brand-blue); line-height: 1; margin-top: 0.35em; }

  .ad__stars { display: block; }
  .ad__title { color: var(--ink); white-space: nowrap; line-height: 1; font-weight: 400; }
  .ad__title .accent { color: var(--brand-blue); }

  .ad__photo {
    background: radial-gradient(closest-side, rgba(47,95,168,0.75) 0%, rgba(143,195,232,0.45) 60%, rgba(143,195,232,0) 100%);
  }

  .offer { color: var(--white); }
  .offer__label { position: absolute; left: 0; top: 0; line-height: 1; white-space: nowrap; }
  .offer__item {
    position: absolute; left: 0;
    display: flex; align-items: center;
    white-space: nowrap; line-height: 1;
    transform: translateY(-50%);
  }
  .offer__icon { flex: none; }
  .offer__icon svg { width: 100%; height: 100%; display: block; }

  .ad__url {
    display: flex; align-items: center; justify-content: center;
    color: var(--white); white-space: nowrap;
    border-radius: 999px;
    background: linear-gradient(180deg, #5fb2e4 0%, var(--blue-deep) 55%, #1577b9 100%);
    border: 2px solid rgba(255,255,255,0.85);
    box-shadow: 8px 10px 12px rgba(10,60,110,0.35);
  }

  /* wide */
  .ad--wide .brand { left: 6%; top: 6%; width: 18%; }
  .ad--wide .brand__dot { width: 112px; height: 112px; }
  .ad--wide .brand__name { font-size: 28px; }
  .ad--wide .ad__stars { left: 51%; top: 3.5%; width: 359px; height: 107px; }
  .ad--wide .ad__title { left: 45.3%; top: 20.5%; font-size: 49px; }
  .ad--wide .ad__photo { left: 3%; top: 46%; width: 47%; height: 50%; }
  .ad--wide .offer { left: 58.5%; top: 36.8%; width: 38%; height: 352px; }
  .ad--wide .offer__label { font-size: 19px; }
  .ad--wide .offer__item { font-size: 28px; gap: 30px; }
  .ad--wide .offer__icon { width: 60px; height: 60px; }
  .ad--wide .offer__item--sale   { top: 20%; }
  .ad--wide .offer__item--buy    { top: 48%; }
  .ad--wide .offer__item--insure { top: 76%; }
  .ad--wide .ad__url { left: 57%; top: 84%; width: 31.5%; height: 6.3%; font-size: 17px; }

  /* tall */
  .ad--tall .brand { left: 4.5%; top: 4.3%; width: 24%; }
  .ad--tall .brand__dot { width: 120px; height: 120px; }
  .ad--tall .brand__name { font-size: 29px; }
  .ad--tall .ad__stars { left: 42.3%; top: 4.5%; width: 357px; height: 106px; }
  .ad--tall .ad__title { left: 35%; top: 20.5%; font-size: 49px; }
  .ad--tall .ad__photo { left: 3%; top: 49%; width: 47%; height: 38%; }
  .ad--tall .offer { left: 53.6%; top: 39.6%; width: 44%; height: 364px; }
  .ad--tall .offer__label { font-size: 20px; }
  .ad--tall .offer__item { font-size: 30px; gap: 34px; }
  .ad--tall .offer__icon { width: 64px; height: 64px; }
  .ad--tall .offer__item--sale   { top: 21%; }
  .ad--tall .offer__item--buy    { top: 50%; }
  .ad--tall .offer__item--insure { top: 80%; }
  .ad--tall .ad__url { left: 51.5%; top: 85.2%; width: 42%; height: 6.3%; font-size: 19px; }

  /* small */
  .ad--small .brand { left: 5.5%; top: 3.5%; width: 18%; }
  .ad--small .brand__dot { width: 76px; height: 76px; }
  .ad--small .brand__name { font-size: 19px; }
  .ad--small .ad__stars { left: 52.7%; top: 3.3%; width: 230px; height: 69px; }
  .ad--small .ad__title { left: 47%; top: 19%; font-size: 31px; }
  .ad--small .ad__photo { left: 3%; top: 42%; width: 46%; height: 52%; }
  .ad--small .offer { left: 58%; top: 37.2%; width: 38%; height: 222px; }
  .ad--small .offer__label { font-size: 14px; }
  .ad--small .offer__item { font-size: 20px; gap: 20px; }
  .ad--small .offer__icon { width: 44px; height: 44px; }
  .ad--small .offer__item--sale   { top: 23%; }
  .ad--small .offer__item--buy    { top: 57%; }
  .ad--small .offer__item--insure { top: 91%; }
  .ad--small .ad__url { left: 56.5%; top: 86.8%; width: 33.5%; height: 6.8%; font-size: 13px; }
</style>
</head>
<body>

<svg width="0" height="0" style="position:absolute">
  <defs>
    <linearGradient id="sea" x1="0" y1="0" x2="0" y2="1">
      <stop offset="0.35" stop-color="#1a84c6"/>
      <stop offset="0.7" stop-color="#56ade0"/>
      <stop offset="1" stop-color="#95d8f3"/>
    </linearGradient>
    <linearGradient id="swoosh" x1="0" y1="0" x2="1" y2="1">
      <stop offset="0" stop-color="#1a84c6"/>
      <stop offset="1" stop-color="#9fdcf5"/>
    </linearGradient>
    <linearGradient id="starfill" x1="0" y1="0" x2="0" y2="1">
      <stop offset="0" stop-color="#8ccbef"/>
      <stop offset="1" stop-color="#2a86c8"/>
    </linearGradient>
    <symbol id="star" viewBox="-1 -1 2 2">
      <polygon points="0,-1 0.235,-0.324 0.951,-0.309 0.38,0.124 0.588,0.809 0,0.4 -0.588,0.809 -0.38,0.124 -0.951,-0.309 -0.235,-0.324" fill="url(#starfill)" stroke="#1f7fc2" stroke-width="0.04"/>
    </symbol>
    <symbol id="stars" viewBox="0 0 400 120">
      <use href="#star" x="2" y="30" width="80" height="80"/>
      <use href="#star" x="60" y="14" width="104" height="104"/>
      <use href="#star" x="136" y="-2" width="128" height="128"/>
      <use href="#star" x="236" y="14" width="104" height="104"/>
      <use href="#star" x="318" y="30" width="80" height="80"/>
    </symbol>
    <symbol id="icon-tag" viewBox="0 0 64 64">
      <g fill="none" stroke="#fff" stroke-width="3" stroke-linejoin="round">
        <path d="M4 6 H34 L40 14 L40 40 L4 40 Z"/>
        <path d="M26 18 L54 30 L60 40 L48 62 L18 48 Z"/>
        <circle cx="52" cy="38" r="2.5"/>
        <path d="M10 30 L20 14"/><circle cx="11" cy="16" r="2.5"/><circle cx="19" cy="28" r="2.5"/>
      </g>
    </symbol>
    <symbol id="icon-cash" viewBox="0 0 64 80">
      <g fill="none" stroke="#fff" stroke-width="3" stroke-linejoin="round" stroke-linecap="round">
        <rect x="4" y="4" width="36" height="66" rx="3"/>
        <rect x="11" y="12" width="22" height="50" rx="2"/>
        <path d="M22 24 V50 M18 31 Q22 27 26 31 Q22 37 18 41 Q22 45 26 41"/>
        <path d="M30 50 L46 44 Q52 46 56 58 L52 72 H34 L34 78 H50"/>
      </g>
    </symbol>
    <symbol id="icon-shield" viewBox="0 0 64 72">
      <g fill="none" stroke="#fff" stroke-width="3" stroke-linejoin="round" stroke-linecap="round">
        <path d="M32 3 L58 12 V34 C58 52 46 63 32 69 C18 63 6 52 6 34 V12 Z"/>
        <path d="M32 11 L50 17 V34 C50 47 42 55 32 60 C22 55 14 47 14 34 V17 Z"/>
        <path d="M22 36 L30 44 L43 29"/>
      </g>
    </symbol>
  </defs>
</svg>

<!-- wide -->
<section class="ad ad--wide">
  <svg class="ad__bg" viewBox="0 0 100 100" preserveAspectRatio="none" aria-hidden="true">
    <path d="M0 26 C8 34 15 36 25 37 C14 38 6 37 0 33 Z" fill="url(#swoosh)"/>
    <path d="M75 30 C85 28 93 29 100 31 L100 36 C92 32 84 30 75 30 Z" fill="url(#swoosh)"/>
    <path d="M0 36 C12 42 28 40 48 36 C68 32 86 31 100 40 L100 100 L0 100 Z" fill="url(#sea)"/>
  </svg>
  <div class="brand"><span class="brand__dot"></span><span class="brand__name">kalvoro.de</span></div>
  <svg class="ad__stars" aria-hidden="true"><use href="#stars"/></svg>
  <h1 class="ad__title">Traktor <span class="accent">Bewertung</span></h1>
  <div class="ad__photo" role="img" aria-label="Foto eines blauen Traktors mit Kabine"></div>
  <div class="offer">
    <p class="offer__label">Kurzgutachen für</p>
    <p class="offer__item offer__item--sale"><span class="offer__icon"><svg><use href="#icon-tag"/></svg></span>Verkauf,</p>
    <p class="offer__item offer__item--buy"><span class="offer__icon"><svg><use href="#icon-cash"/></svg></span>Kauf oder</p>
    <p class="offer__item offer__item--insure"><span class="offer__icon"><svg><use href="#icon-shield"/></svg></span>Versicherung</p>
  </div>
  <p class="ad__url">www.kalvoro.de/traktorwert</p>
</section>

<!-- tall -->
<section class="ad ad--tall">
  <svg class="ad__bg" viewBox="0 0 100 100" preserveAspectRatio="none" aria-hidden="true">
    <path d="M0 25 C9 32 18 34 34 34 C18 35 7 34 0 31 Z" fill="url(#swoosh)"/>
    <path d="M75 29.5 C86 28.5 94 29 100 30.5 L100 34 C92 31 84 30 75 29.5 Z" fill="url(#swoosh)"/>
    <path d="M0 33 C14 39 30 37 50 33 C70 29.5 88 29 100 34.5 L100 100 L0 100 Z" fill="url(#sea)"/>
  </svg>
  <div class="brand"><span class="brand__dot"></span><span class="brand__name">kalvoro.de</span></div>
  <svg class="ad__stars" aria-hidden="true"><use href="#stars"/></svg>
  <h1 class="ad__title">Traktor <span class="accent">Bewertung</span></h1>
  <div class="ad__photo" role="img" aria-label="Foto eines blauen Traktors ohne Kabine"></div>
  <div class="offer">
    <p class="offer__label">Kurzgutachen für</p>
    <p class="offer__item offer__item--sale"><span class="offer__icon"><svg><use href="#icon-tag"/></svg></span>Verkauf,</p>
    <p class="offer__item offer__item--buy"><span class="offer__icon"><svg><use href="#icon-cash"/></svg></span>Kauf oder</p>
    <p class="offer__item offer__item--insure"><span class="offer__icon"><svg><use href="#icon-shield"/></svg></span>Versicherung</p>
  </div>
  <p class="ad__url">www.kalvoro.de/traktorwert</p>
</section>

<!-- small -->
<section class="ad ad--small">
  <svg class="ad__bg" viewBox="0 0 100 100" preserveAspectRatio="none" aria-hidden="true">
    <path d="M0 23 C9 33 20 35 34 34 C18 37 7 35 0 32 Z" fill="url(#swoosh)"/>
    <path d="M75 29 C86 28 94 29 100 30.5 L100 35 C92 31 84 29.5 75 29 Z" fill="url(#swoosh)"/>
    <path d="M0 33 C14 40 30 38 50 33.5 C70 29.5 88 29 100 37.5 L100 100 L0 100 Z" fill="url(#sea)"/>
  </svg>
  <div class="brand"><span class="brand__dot"></span><span class="brand__name">kalvoro.de</span></div>
  <svg class="ad__stars" aria-hidden="true"><use href="#stars"/></svg>
  <h1 class="ad__title">Traktor <span class="accent">Bewertung</span></h1>
  <div class="ad__photo" role="img" aria-label="Foto eines blauen Traktors mit Kabine"></div>
  <div class="offer">
    <p class="offer__label">Kurzgutachen für</p>
    <p class="offer__item offer__item--sale"><span class="offer__icon"><svg><use href="#icon-tag"/></svg></span>Verkauf,</p>
    <p class="offer__item offer__item--buy"><span class="offer__icon"><svg><use href="#icon-cash"/></svg></span>Kauf oder</p>
    <p class="offer__item offer__item--insure"><span class="offer__icon"><svg><use href="#icon-shield"/></svg></span>Versicherung</p>
  </div>
  <p class="ad__url">www.kalvoro.de/traktorwert</p>
</section>

</body>
</html>
```